Honey Labels for Manuka, Rewarewa, Multifloral and Manuka Blend honey

We require 4 label designs for our 4 types of honey i.e. Manuka, Rewarewa, Multifloral and Manuka Blend. Each design should be adapted for 250g, 500g, and 1kg PET jars. The design should look friendly and professional.

Tare: amber Square mason PET jars (see images attached)
Jar dimensions: see PDF attached

Target Market(s)

Worldwide. People caring for their health.

Industry/Entity Type

Health Product

Font styles to use
Serif
Decorative

Colors
6a429a
f37122
0692cd
9bcb3c

Requirements
Must have
• Each label should contain the following information
• • name of the honey e.g. Manuka Honey
• • VelloraTM logo (provided)
• • an image of a bird (provided),
• • nutrition table
• • a bar code
• • a place for a batch number and the best before date to be printed
• • volume: e.g. 250g, 500g, 1kg
• • Text: “Product of New Zealand”
• • Text: “Produced & packed by: Pemrick’s Hives Ltd. 48B Kolhurst Road, Tauranga 3162, New Zealand sales@vellorahoney.co.nz www.vellorahoney.co.nz
• • Ingredients: 100% Pure Raw New Zealand Honey
• • Text: “All specified values are averages.”
• • Not suitable for infants under 12 months. Do not use if cap seal is broken. Production methods involved with this product are not-GM. Contains bee products.
• • PET Recycling pictogram
• • Round corners
• Apart from different bird image each of 4 honey labels should have it's own color element e.g a different color background or a line.
• The birds:
• • Manuka honey: image of a Kingfisher bird
• o MGO Pictogram (80+, 100+, 200+, 300+ or 400+)
• • Rewarewa honey: image of a Kereru bird
• • Multifloral honey: image of a Tui bird
• • Manuka blend: image of a Pukekohe bird
Should not have
• Disclaimer: The provided images of birds is a copyright content. It is prohibited to use them outside of this project.

```html
<!DOCTYPE html>
<html lang="en">
<head>
<meta charset="utf-8">
<title>Vellora Rewarewa Honey – 1 Kg Label</title>
<link href="https://fonts.googleapis.com/css2?family=Arimo:wght@400;700&family=Pinyon+Script&family=Cinzel:wght@500&display=swap" rel="stylesheet">
<style>
  :root {
    --canvas: #ffffff;
    --label-top: #7c0a4c;
    --label-bottom: #560234;
    --band: #231f20;
    --band-shadow: #3a0420;
    --gold: #c7a15a;
    --ink: #ffffff;
    --muted: #a0607f;
    --bird-a: #3fb8a0;
    --bird-b: #5a3d9a;
    --bird-c: #e8e4ee;
  }
  * { margin: 0; padding: 0; box-sizing: border-box; }
  html, body { width: 1200px; height: 1000px; overflow: hidden; background: var(--canvas); }
  body { position: relative; font-family: "Arimo", Arial, sans-serif; color: var(--ink); }

  .label {
    position: absolute; left: 37px; top: 145px; width: 1124px; height: 328px;
    background: linear-gradient(180deg, var(--label-top), var(--label-bottom));
    overflow: hidden;
  }
  .label__band { position: absolute; inset: 0; width: 1124px; height: 328px; }

  .producer {
    position: absolute; left: 18px; top: 30px; width: 340px;
    text-align: center; font-size: 12.5px; line-height: 20px; letter-spacing: 0.2px;
  }
  .producer p + p { margin-top: 20px; }

  .brand {
    position: absolute; left: 501px; top: 24px; width: 120px;
    display: flex; align-items: center; justify-content: center; gap: 6px;
    font-family: "Cinzel", Georgia, serif; font-weight: 500; font-size: 14px;
    letter-spacing: 1.5px; color: var(--gold);
  }
  .brand__dot { width: 7px; height: 7px; border-radius: 50%; background: var(--gold); }

  .product-name {
    position: absolute; left: 436px; top: 142px;
    font-family: "Pinyon Script", cursive; font-size: 36px; color: var(--gold);
    white-space: nowrap;
  }
  .origin {
    position: absolute; left: 391px; top: 293px;
    font-size: 10.5px; line-height: 13px; color: var(--muted);
  }

  .bird-art {
    position: absolute; left: 680px; top: 128px; width: 112px; height: 200px;
    background: linear-gradient(160deg, var(--bird-a) 0%, var(--bird-b) 55%, var(--bird-c) 100%);
    border-radius: 50% 50% 30% 30% / 30% 30% 20% 20%;
    opacity: 0.9;
  }

  .facts { position: absolute; left: 846px; top: 20px; width: 214px; text-align: center; }
  .facts__heading { font-size: 9.5px; text-decoration: underline; }
  .facts__ingredients { font-size: 9.5px; margin-top: 4px; }

  .nutrition {
    margin-top: 6px; width: 206px; margin-left: 4px;
    border: 1px solid var(--ink); border-radius: 8px; padding: 5px 8px 6px;
    font-size: 9px;
  }
  .nutrition__title { line-height: 15px; }
  .nutrition table { width: 100%; border-collapse: collapse; font-size: 7px; margin-top: 4px; }
  .nutrition thead th { font-weight: 400; line-height: 11px; padding: 3px 0 4px; border-top: 1px solid var(--ink); border-bottom: 1px solid var(--ink); }
  .nutrition td { line-height: 11px; text-align: center; }
  .nutrition td:first-child { text-align: left; }
  .nutrition tbody tr:first-child td { padding-top: 3px; }

  .notice { font-size: 7.5px; line-height: 12px; margin-top: 8px; }
  .notice--warnings { margin-top: 12px; }
</style>
</head>
<body>
  <section class="label" aria-label="Rewarewa Honey 1 Kg jar label">
    <svg class="label__band" viewBox="0 0 1124 328" aria-hidden="true">
      <path d="M0 0 H1124 V12 Q1000 0 818 20 Q560 135 308 20 Q150 0 0 14 Z" fill="var(--band-shadow)"/>
      <path d="M0 0 H1124 V4 Q1000 -4 815 14 Q560 115 310 14 Q150 -4 0 6 Z" fill="var(--band)"/>
    </svg>

    <div class="producer">
      <p>This honey is sourced from the New Zealand Manuka tree. Each batch of Vellora honey has been tested by independent scientific laboratory for non preoxide activity and Methylglyoxal (MGO) content.</p>
      <p>Produced &amp; packed by:<br>Pemrick’s Hives Ltd. 48B Kolhurst Road, Tauranga 3162,<br>New Zealand</p>
      <p>sales@vellorahoney.co.nz<br>www.vellorahoney.co.nz</p>
    </div>

    <div class="brand"><span class="brand__dot"></span>VELLORA</div>

    <h1 class="product-name">Rewarewa Honey</h1>
    <p class="origin">Product of New Zealand<br>1 Kg</p>

    <div class="bird-art" role="img" aria-label="Faceted illustration of a Kereru bird perched, in teal, violet and white tones"></div>

    <div class="facts">
      <p class="facts__heading">Ingridients:</p>
      <p class="facts__ingredients">100% Pure Raw New Zealand Honey</p>
      <div class="nutrition">
        <p class="nutrition__title">Nutrition Information<br>Serving per package: 50<br>Serving size : 10g</p>
        <table>
          <thead>
            <tr><th></th><th>Average<br>quantity<br>serving</th><th>Average<br>quantity<br>per 100g</th></tr>
          </thead>
          <tbody>
            <tr><td>Energy</td><td>132KJ</td><td>1320 KJ</td></tr>
            <tr><td>Protein</td><td>Less than 1g</td><td>0.4g</td></tr>
            <tr><td>Fat,Total</td><td>0g</td><td>0g</td></tr>
            <tr><td>-saturated</td><td>0g</td><td>0g</td></tr>
            <tr><td>Carbohydrate</td><td>8g</td><td>80g</td></tr>
            <tr><td>-sugars</td><td>7.8g</td><td>78g</td></tr>
            <tr><td>Sodium</td><td>1.2g</td><td>120g</td></tr>
          </tbody>
        </table>
      </div>
      <p class="notice">All specified values are averages.</p>
      <p class="notice notice--warnings">Not suitable for infants under 12 months.<br>Do not use if cap seal is broken.<br>Production methods involved with this product.<br>are not-GM. Contains bee products.</p>
    </div>
  </section>
</body>
</html>
```